TECH PROJECT NEEDS NEW SKINS FOR RE-BRANDING

We are a technology project that has a product (crypto wallet) nearing release, have basic designs made so far however we need NEW SKINS/ branding/ design options for this wallet to change the look and feel -- it will be called and re-branded as "KESTRIL" a futuristic/ space/ edgy product so need it to look like so.

YOU ARE ALLOWED TO CHANGE + EXPERIMENT WITH THE LAYOUT/ schema and UI as you see fit -- (we are open to new and creative ideas)

(see WALLET.PNG and PROTFOLIO.PNG ATTACHED --- these are the pages we need new skins for )

(see KESTRIL logo attached --- PLEASE USE THIS LOGO/ VERSIONS OF THIS LOGO IN YOUR DESIGNS/SKIN SUBMISSIONS -- WE PROVIDED THE ai file so feel free to alter the logo a bit to experiment if you want -- we are open and flexible to new creative ideas)

(FOR A MOOD BOARD FOR GUIDANCE on feel/colors/mood-- SEE "SAMPLE INTERFACE 1 & 2" ATTACHED)

Target Market(s)

TECHNOLOGY/SPACE/ FUTURE

Number of Pages Required

2 page

Colors

Designer to choose colors to be used in the design.

Requirements
Must have
• MUST USE OUR KESTRIL LOGO OR A SIMILAR ALTERATION OF IT

```html
<!DOCTYPE html>
<html lang="en">
<head>
<meta charset="utf-8">
<title>KESTRIL Wallet</title>
<link rel="stylesheet" href="https://fonts.googleapis.com/css2?family=Roboto:wght@400;500;700&display=swap">
<style>
:root{
  --backdrop:#113039;
  --nav-bg:#1e3a44;
  --tab:#3b5661;
  --tab-dark:#0e1a24;
  --list-bg:#0e1a26;
  --main-bg:#10283a;
  --accent-blue:#1f6de0;
  --accent-teal:#3fb8a6;
  --orange:#f26a2e;
  --text:#e8eef2;
  --muted:#8a9aa5;
  --row-send:#3a474f;
  --row-recv:#1b3f46;
  --success:#35d0b0;
}
*{box-sizing:border-box;margin:0;padding:0}
html,body{width:1200px;height:960px;overflow:hidden}
body{background:var(--backdrop);font-family:'Roboto',sans-serif;color:var(--text);position:relative}
.app{position:absolute;left:54px;top:173px;width:1093px;height:614px;overflow:hidden;background:var(--main-bg);box-shadow:0 10px 40px rgba(0,0,0,.45)}

/* nav */
.nav{position:absolute;left:0;top:0;width:91px;height:100%;background:var(--nav-bg);border-right:1px solid #2d7f82}
.brand{position:absolute;left:0;top:30px;width:91px;text-align:center;font-weight:700;font-size:12px;letter-spacing:1.5px}
.brand::before{content:"";display:block;width:18px;height:18px;margin:0 auto 6px;border:2px solid var(--text);border-radius:50%}
.tab{position:absolute;left:0;width:80px;background:var(--tab);font-size:10px;font-weight:500;text-align:center;display:flex;flex-direction:column;align-items:center;justify-content:center;gap:6px;
  clip-path:polygon(0 0,68px 0,80px 10px,80px 100%,0 100%)}
.tab svg{width:22px;height:22px;fill:none;stroke:#c8d3d8;stroke-width:1.3}
.tab.settings{background:var(--tab-dark);border:1px solid #3b5661}

/* wallet list */
.wallet{position:absolute;left:91px;top:0;width:272px;height:100%;background:var(--list-bg);border-right:1px solid #2d7f82}
.wallet h1{position:absolute;left:49px;top:51px;font-size:22px;font-weight:700;letter-spacing:.5px}
.frame{position:absolute}
.corner{position:absolute;width:12px;height:12px;border-color:var(--accent-teal);border-style:solid;border-width:0}
.c-tl{left:0;top:0;border-left-width:2px;border-top-width:2px}
.c-tr{right:0;top:0;border-right-width:2px;border-top-width:2px}
.c-bl{left:0;bottom:0;border-left-width:2px;border-bottom-width:2px}
.c-br{right:0;bottom:0;border-right-width:2px;border-bottom-width:2px}
.search{position:absolute;background:#0a141d;font-size:10px;color:var(--orange)}
.search span{position:absolute;left:8px;top:14px}
.search::after{content:"";position:absolute;left:8px;right:16px;bottom:2px;height:1px;background:var(--orange)}
.search svg{position:absolute;right:18px;top:9px;width:14px;height:14px;fill:none;stroke:var(--orange);stroke-width:1.4}
.coin{position:absolute;left:45px;width:185px;height:40px;background:#0c1822;border:1px solid #1c2e3a;font-size:10px}
.coin.active{background:#133166;border-color:#1d4a9a}
.coin.highlight{border-color:var(--orange)}
.coin .dot{position:absolute;left:7px;top:9px;width:22px;height:22px;border-radius:50%;background:var(--c)}
.coin .name{position:absolute;left:38px;top:8px;font-weight:500;color:var(--c)}
.coin .amt{position:absolute;left:38px;top:23px;color:var(--muted)}

/* header */
.header{position:absolute;left:387px;top:19px;width:681px;height:57px;background:linear-gradient(90deg,#143a66,#10305a);border:1px solid var(--accent-blue)}
.header .dot{position:absolute;left:13px;top:13px;width:30px;height:30px;border-radius:50%;background:#1c4e9a;border:1px solid #2d73d6}
.header h2{position:absolute;left:66px;top:17px;font-size:21px;font-weight:700;color:var(--accent-blue);letter-spacing:.3px}
.header h2 b{color:var(--text)}
.rate{position:absolute;left:426px;top:13px;width:242px;height:31px;background:#0f2340;border:1px solid #1c3d6a;font-size:9px;text-align:right;padding:10px 18px 0 0}
.rule{position:absolute;left:363px;right:0;height:1px;background:#2a5f6a}

/* balance */
.balance{position:absolute;left:387px;top:117px;width:387px;height:143px;background:#13345a}
.label{position:absolute;font-size:9px;color:var(--accent-blue)}
.bal-box{position:absolute;left:23px;top:32px;width:339px;height:50px;background:#0b1626;border:1px solid #1c3a6a}
.bal-box strong{position:absolute;left:11px;top:6px;font-size:19px;font-weight:500}
.bal-box em{position:absolute;left:11px;top:31px;font-style:normal;font-size:10px;color:var(--accent-blue)}
.addr{position:absolute;left:27px;top:112px;font-size:9px}
.copy{position:absolute;right:27px;top:112px;font-size:9px;color:var(--orange)}

/* actions */
.actions{position:absolute;left:802px;top:117px;width:262px;height:143px;background:#2b3b43}
.btn{position:absolute;top:16px;width:113px;height:64px;font-size:10px;font-weight:700;text-align:center;padding-top:12px}
.btn svg{display:block;margin:8px auto 0;width:26px;height:28px;fill:none;stroke:#e8eef2;stroke-width:1.4}
.btn.send{left:11px;background:#8a979d;clip-path:polygon(0 0,100% 0,100% 82%,86% 100%,0 100%)}
.btn.recv{left:138px;background:#0e1a24;border:1px solid #c8d3d8}

/* table */
.thead{position:absolute;left:387px;top:299px;width:675px;height:49px;border:1px solid var(--accent-teal);background:#10263a;font-size:9px;color:#b9c5cb}
.thead span,.row span{position:absolute}
.thead span{top:20px}
.row{position:absolute;left:387px;width:675px;height:32px;font-size:9.5px}
.row.send{background:var(--row-send)}
.row.recv{background:var(--row-recv)}
.row span{top:11px}
.row .act{left:29px}
.row.recv .act{color:var(--success)}
.row .id{color:#9aa7ad}
.row .pending{color:var(--orange)}
.row .success{color:var(--success)}
.row svg{position:absolute;left:4px;top:5px;width:18px;height:20px;fill:none;stroke-width:1.2}
.row.send svg{stroke:#e8eef2}
.row.recv svg{stroke:var(--success)}
.details{position:absolute;left:605px;top:5px;width:64px;height:22px;background:#17427e;border:1px solid #1f5fc0;color:#2f7be8;font-size:9px;font-style:normal;text-align:center;line-height:20px}
</style>
</head>
<body>
<main class="app">
  <nav class="nav">
    <div class="brand">KESTRIL</div>
    <div class="tab" style="top:97px;height:65px">
      <svg viewBox="0 0 24 24"><rect x="3" y="3" width="8" height="8"/><rect x="13" y="3" width="8" height="8"/><rect x="3" y="13" width="8" height="8"/><rect x="13" y="13" width="8" height="8"/></svg>Dashboard</div>
    <div class="tab" style="top:170px;height:66px">
      <svg viewBox="0 0 24 24"><path d="M3 3v18h18M6 16l4-5 3 3 6-7"/></svg>Portfolio</div>
    <div class="tab" style="top:242px;height:65px">
      <svg viewBox="0 0 24 24"><rect x="4" y="3" width="16" height="18"/><path d="M4 9h16M14 13h6v4h-6z"/></svg>Wallet</div>
    <div class="tab" style="top:316px;height:66px">
      <svg viewBox="0 0 24 24"><path d="M14 2L6 13h5l-2 9 9-12h-5z"/></svg>Lightning</div>
    <div class="tab" style="top:391px;height:66px">
      <svg viewBox="0 0 24 24"><path d="M6 18h12a4 4 0 0 0 0-8 6 6 0 0 0-11-1 4.5 4.5 0 0 0-1 9z"/></svg>NVK Cloud</div>
    <div class="tab settings" style="top:467px;height:56px">
      <svg viewBox="0 0 24 24"><circle cx="12" cy="12" r="3.5"/><path d="M12 2l2 3 3.5-1 .5 3.5 3 2-2 3 2 3-3 2-.5 3.5-3.5-1-2 3-2-3-3.5 1-.5-3.5-3-2 2-3-2-3 3-2 .5-3.5 3.5 1z"/></svg></div>
  </nav>

  <section class="wallet">
    <h1>WALLET</h1>
    <div class="frame" style="left:20px;top:97px;width:233px;height:427px">
      <i class="corner c-tl"></i><i class="corner c-tr"></i><i class="corner c-bl"></i><i class="corner c-br"></i>
    </div>
    <div class="search" style="left:45px;top:136px;width:184px;height:32px">
      <span>Search...</span>
      <svg viewBox="0 0 16 16"><circle cx="6" cy="6" r="4.5"/><path d="M9.5 9.5L15 15"/></svg>
    </div>
    <div class="coin highlight" style="top:188px;--c:#f26a2e"><i class="dot"></i><span class="name">Orbalis - ORB</span><span class="amt">369,800.00 ORB</span></div>
    <div class="coin" style="top:238px;--c:#2f8ee8"><i class="dot"></i><span class="name">DART - DRT</span><span class="amt">369,800.00 DRT</span></div>
    <div class="coin" style="top:289px;--c:#8a3cf0"><i class="dot"></i><span class="name">AURELION - AUR</span><span class="amt">369,800.00 AUR</span></div>
    <div class="coin" style="top:339px;--c:#c8d0d5"><i class="dot" style="background:#5c6a72"></i><span class="name">LUMACOIN - LMC</span><span class="amt">369,800.00 LMC</span></div>
    <div class="coin" style="top:390px;--c:#8fb7dd"><i class="dot" style="background:#3d6d9a"></i><span class="name">RIVULET - RVL</span><span class="amt">369,800.00 RVL</span></div>
    <div class="coin active" style="top:441px;--c:#e8eef2"><i class="dot" style="background:#1f6de0"></i><span class="name">NOVASTAK - NVK</span><span class="amt">369,800.00 NVK</span></div>
  </section>

  <header class="header">
    <i class="dot"></i>
    <h2>NOVASTAK - <b>NVK</b></h2>
    <div class="rate">1 NVK = 0.08 USD</div>
  </header>
  <div class="rule" style="top:98px"></div>

  <section class="balance">
    <div class="frame" style="left:0;top:0;width:387px;height:143px">
      <i class="corner c-tl"></i><i class="corner c-tr"></i><i class="corner c-bl"></i><i class="corner c-br"></i>
    </div>
    <span class="label" style="left:27px;top:13px">Balance</span>
    <div class="bal-box"><strong>369.000 NVK</strong><em>= 29.584 00 USD</em></div>
    <span class="label" style="left:27px;top:96px">Wallet Address</span>
    <span class="addr">TgjkbLN m27g3 IkkkBkLkJgbk</span>
    <span class="copy">Copy</span>
  </section>

  <section class="actions">
    <div class="frame" style="left:0;top:0;width:262px;height:143px">
      <i class="corner c-tl"></i><i class="corner c-tr"></i><i class="corner c-bl"></i><i class="corner c-br"></i>
    </div>
    <div class="btn send">SEND MONEY
      <svg viewBox="0 0 26 28"><path d="M13 1l11 6.5v13L13 27 2 20.5v-13z"/><path d="M13 20V9M9 13l4-4 4 4"/></svg></div>
    <div class="btn recv">RECEIVE MONEY
      <svg viewBox="0 0 26 28"><path d="M13 1l11 6.5v13L13 27 2 20.5v-13z"/><path d="M13 8v11M9 15l4 4 4-4"/></svg></div>
    <div class="search" style="left:11px;top:94px;width:242px;height:32px">
      <span>Search...</span>
      <svg viewBox="0 0 16 16"><circle cx="6" cy="6" r="4.5"/><path d="M9.5 9.5L15 15"/></svg>
    </div>
  </section>
  <div class="rule" style="top:281px"></div>

  <div class="thead">
    <span style="left:13px">ACTIVITY</span><span style="left:125px">DATE</span><span style="left:181px">TRANSACTION ID</span>
    <span style="left:313px">AMOUNT</span><span style="left:391px">STATUS</span><span style="left:474px">BALANCE CHANGE</span><span style="left:618px">DETAILS</span>
  </div>

  <div class="row send" style="top:356px"><svg viewBox="0 0 18 20"><path d="M9 1l8 4.5v9L9 19 1 14.5v-9z"/><path d="M9 14V6M6 9l3-3 3 3"/></svg><span class="act">Sending Money</span><span style="left:122px">11.03.19</span><span class="id" style="left:181px">TgjkbLN m27ggvKhn637d...</span><span style="left:316px">43.00 NVK</span><span class="pending" style="left:391px">Pending</span><span style="left:474px">369,800.00 NVK</span><i class="details">DETAILS</i></div>
  <div class="row recv" style="top:396px"><svg viewBox="0 0 18 20"><path d="M9 1l8 4.5v9L9 19 1 14.5v-9z"/><path d="M9 6v8M6 11l3 3 3-3"/></svg><span class="act">Receiving Money</span><span style="left:122px">11.03.19</span><span class="id" style="left:181px">TgjkbLN m27ggvKhn637d...</span><span style="left:314px">43.00 NVK</span><span class="success" style="left:391px">Success</span><span style="left:474px">369,800.00 NVK</span><i class="details">DETAILS</i></div>
  <div class="row send" style="top:436px"><svg viewBox="0 0 18 20"><path d="M9 1l8 4.5v9L9 19 1 14.5v-9z"/><path d="M9 14V6M6 9l3-3 3 3"/></svg><span class="act">Sending Money</span><span style="left:122px">11.03.19</span><span class="id" style="left:181px">TgjkbLN m27ggvKhn637d...</span><span style="left:314px">43.00 NVK</span><span class="success" style="left:391px">Success</span><span style="left:474px">369,800.00 NVK</span><i class="details">DETAILS</i></div>
  <div class="row recv" style="top:476px"><svg viewBox="0 0 18 20"><path d="M9 1l8 4.5v9L9 19 1 14.5v-9z"/><path d="M9 6v8M6 11l3 3 3-3"/></svg><span class="act">Receiving Money</span><span style="left:122px">11.03.19</span><span class="id" style="left:181px">TgjkbLN m27ggvKhn637d...</span><span style="left:314px">43.00 NVK</span><span class="pending" style="left:391px">Pending</span><span style="left:474px">369,800.00 NVK</span><i class="details">DETAILS</i></div>
  <div class="row send" style="top:516px"><svg viewBox="0 0 18 20"><path d="M9 1l8 4.5v9L9 19 1 14.5v-9z"/><path d="M9 14V6M6 9l3-3 3 3"/></svg><span class="act">Sending Money</span><span style="left:122px">11.03.19</span><span class="id" style="left:181px">TgjkbLN m27ggvKhn637d...</span><span style="left:314px">43.00 NVK</span><span class="success" style="left:391px">Success</span><span style="left:474px">369,800.00 NVK</span><i class="details">DETAILS</i></div>
  <div class="row recv" style="top:556px"><svg viewBox="0 0 18 20"><path d="M9 1l8 4.5v9L9 19 1 14.5v-9z"/><path d="M9 6v8M6 11l3 3 3-3"/></svg><span class="act">Receiving Money</span><span style="left:122px">11.03.19</span><span class="id" style="left:181px">TgjkbLN m27ggvKhn637d...</span><span style="left:314px">43.00 NVK</span><span class="success" style="left:391px">Success</span><span style="left:474px">369,800.00 NVK</span><i class="details">DETAILS</i></div>
  <div class="row recv" style="top:596px"><svg viewBox="0 0 18 20"><path d="M9 1l8 4.5v9L9 19 1 14.5v-9z"/><path d="M9 6v8M6 11l3 3 3-3"/></svg><span class="act">Receiving Money</span><span style="left:122px">11.03.19</span><span class="id" style="left:181px">TgjkbLN m27ggvKhn637d...</span><span style="left:314px">43.00 NVK</span><span class="success" style="left:391px">Success</span><span style="left:474px">369,800.00 NVK</span><i class="details">DETAILS</i></div>
</main>
</body>
</html>
```